Modern Retail Coffee Label for established Roastery! 17 years!

We are looking for a Retail Coffee Bag Label... JUST THE LABEL TO GO ON AN EXISTING BAG. Our current label is provided and our Logo.. we have had the same Red Bags FOREVER so we are looking for a label to compliment that tradition and to be placed on the bags we have used for 17 years.

We have a retail line of bags with locally roasted coffee. Our business has been around 17years and is in need of a design upgrade! We have a red coffee bag and are looking for a sleek modern label. I will attach a file of our label right now so you can see what it looks like. We are just looking for a more modern version. a few inclusions:

Locally Roasted
100% Arabica Coffee
Heron Kin's Coffee
heronkincoffee.example
logo

The black label with the red and yellow color label is the old one... the new label should be the White background and black border one...

Target Market(s)

Retail Coffee Consumers

Font styles to use
Other font styles liked:
• use what you think. we are located in SW Wisconsin but ship coffee EVERYWHERE

Colors

Designer to choose only greyscale colors for use in the design.

Requirements
Must have
• Locally Roasted (Alderton,WI)
• 100% Arabica Coffee
• heronkincoffee.example
• logo
Nice to have
• Badgers
• "Since 2005"
Should not have
• Any lunabrew or big brand themes

```html
<!DOCTYPE html>
<html lang="en">
<head>
<meta charset="utf-8">
<title>Heron Kin's Coffee – Retail Bag Label</title>
<link rel="stylesheet" href="https://fonts.googleapis.com/css2?family=Anton&family=Montserrat:wght@200;600&family=Open+Sans:wght@500&display=swap">
<style>
  :root {
    --ink: #161a1b;
    --paper: #ffffff;
    --muted: #3a3d3f;
    --roast-dark: #6e3f16;
    --roast-light: #d4a752;
  }
  * { margin: 0; padding: 0; box-sizing: border-box; }
  html, body {
    width: 920px;
    height: 1200px;
    overflow: hidden;
    background: var(--paper);
  }
  .label {
    position: relative;
    width: 920px;
    height: 1200px;
    background: var(--paper);
    color: var(--ink);
  }
  .label-frame {
    position: absolute;
    inset: 0;
  }
  .brand-name,
  .brand-product {
    position: absolute;
    left: 0;
    width: 100%;
    text-align: center;
    font-family: "Anton", sans-serif;
    text-transform: uppercase;
    color: var(--ink);
    white-space: nowrap;
    line-height: 1;
  }
  .brand-name {
    top: 88px;
    font-size: 140px;
    letter-spacing: 16px;
    padding-left: 16px;
  }
  .brand-product {
    top: 332px;
    font-size: 140px;
    letter-spacing: 14px;
    padding-left: 14px;
  }
  .brand-illustration {
    position: absolute;
    left: 279px;
    top: 241px;
    width: 348px;
    height: 93px;
    border-radius: 46px 46px 10px 10px;
    background: linear-gradient(90deg, var(--roast-light) 0%, var(--roast-dark) 30%, var(--roast-dark) 70%, var(--roast-light) 100%);
  }
  .origin-claim {
    position: absolute;
    top: 540px;
    left: 0;
    width: 100%;
    text-align: center;
    font-family: "Montserrat", sans-serif;
    font-weight: 600;
    font-size: 27px;
    letter-spacing: -1px;
  }
  .rule {
    position: absolute;
    left: 103px;
    width: 712px;
    height: 4px;
    border-radius: 2px;
    background: var(--ink);
  }
  .rule--top { top: 632px; }
  .rule--bottom { top: 887px; }
  .roastery-details {
    position: absolute;
    top: 966px;
    left: 0;
    width: 100%;
    text-align: center;
    font-family: "Montserrat", sans-serif;
    font-weight: 200;
    font-size: 28px;
    line-height: 31px;
    color: var(--muted);
  }
  .roastery-site {
    position: absolute;
    top: 1032px;
    left: 0;
    width: 100%;
    text-align: center;
    font-family: "Open Sans", sans-serif;
    font-weight: 500;
    font-size: 28px;
    color: var(--ink);
  }
</style>
</head>
<body>
  <main class="label">
    <svg class="label-frame" width="920" height="1200" viewBox="0 0 920 1200" aria-hidden="true">
      <path d="M57,10 L866,8 C900,8 912,60 912,125 L910,1075 C912,1150 895,1188 865,1188 L57,1190 C25,1190 12,1150 8,1125 L8,72 C14,42 28,10 57,10 Z"
            fill="none" stroke="var(--ink)" stroke-width="11" stroke-linejoin="round"/>
    </svg>

    <h1 class="brand-name">Heron Kin's</h1>
    <div class="brand-illustration" role="img" aria-label="Illustration of two animals facing each other above the word Coffee"></div>
    <div class="brand-product">Coffee</div>

    <p class="origin-claim">100% ARABICA COFFEE</p>

    <div class="rule rule--top"></div>
    <div class="rule rule--bottom"></div>

    <p class="roastery-details">Since 2005<br>Locally Roasted (Alderton,WI)</p>
    <p class="roastery-site">www.heronkincoffee.example</p>
  </main>
</body>
</html>
```